Business Cards Needed For Veterinary Business

Looking for a business card design for a veterinary blood bank. We would like it to be clean and professional on appearance but still warm and inviting. We would like to utilize our logo and similar coloring. We will use our phone number, email, website, employee name, employee title.

We do not want a bunch of animated animal photos but do not need the style to be as clinical as a laboratory or human medical procedure office.

We are looking for some creative ideas to choose from so that we can generate a standout professional business card for our management team to utilize.

Target Market(s)

professionals

Industry/Entity Type

veterinary

Contact Information for Business Card

employee name, employee title, phone number, website URL, email

Font styles to use
Sans Serif

Colors
0054AA
0677BA
7BADD7
CADEEF
E8F1F8
EB3D1F
EC4F4E
F09395
F8D3D4
FCEDEE

Requirements
Nice to have
• creative design
Should not have
• animated photos

```html
<!DOCTYPE html>
<html lang="en">
<head>
<meta charset="utf-8">
<title>Harborview Animal Blood Bank – Business Cards</title>
<link href="https://fonts.googleapis.com/css2?family=Montserrat:wght@400;700;800&display=swap" rel="stylesheet">
<style>
  :root {
    --navy: #0054AA;
    --deep-navy: #1a3a7a;
    --red: #EB3D1F;
    --red-soft: #EC4F4E;
    --ink: #3a3a3a;
    --paper: #ffffff;
    --stage: #d4d7d9;
    --edge: #1f3fa8;
  }
  * { box-sizing: border-box; margin: 0; padding: 0; }
  html, body { width: 1200px; height: 829px; overflow: hidden; }
  body {
    background: var(--stage);
    font-family: "Montserrat", sans-serif;
    position: relative;
  }
  .card {
    position: absolute;
    width: 520px;
    height: 297px;
    background: var(--paper);
    border-bottom: 5px solid var(--edge);
    box-shadow: 0 10px 24px rgba(0,0,0,0.18);
  }
  .card--front { left: 50px; top: 266px; }
  .card--back  { left: 630px; top: 266px; }

  .brand {
    display: flex;
    align-items: center;
    gap: 12px;
  }
  .brand__dot {
    width: 30px; height: 30px;
    border-radius: 50%;
    background: var(--red);
    flex: none;
  }
  .brand__name {
    color: var(--red);
    font-weight: 800;
    text-transform: uppercase;
    line-height: 1.05;
  }

  .card--front .brand { position: absolute; left: 150px; top: 42px; }
  .card--front .brand__name { font-size: 21px; }

  .card--back .brand { position: absolute; left: 70px; top: 115px; }
  .card--back .brand__dot { width: 40px; height: 40px; }
  .card--back .brand__name { font-size: 27px; }

  .person {
    position: absolute;
    right: 290px;
    top: 148px;
    text-align: right;
  }
  .person__name {
    color: var(--navy);
    font-weight: 800;
    font-size: 18px;
    letter-spacing: 0.5px;
    text-transform: uppercase;
  }
  .person__title {
    color: var(--ink);
    font-size: 12px;
    margin-top: 2px;
  }
  .divider {
    position: absolute;
    left: 245px;
    top: 142px;
    width: 1px;
    height: 68px;
    background: #9a9a9a;
  }
  .contact {
    position: absolute;
    left: 262px;
    top: 144px;
    list-style: none;
  }
  .contact li {
    display: flex;
    align-items: center;
    gap: 8px;
    font-size: 13px;
    color: var(--ink);
    height: 22px;
  }
  .contact svg { width: 11px; height: 11px; fill: var(--red-soft); flex: none; }
  .address {
    position: absolute;
    left: 0; right: 0;
    bottom: 34px;
    text-align: center;
    font-size: 13px;
    color: var(--ink);
  }
</style>
</head>
<body>

<section class="card card--front" aria-label="Business card front">
  <div class="brand">
    <span class="brand__dot"></span>
    <span class="brand__name">Harborview Animal<br>Blood Bank</span>
  </div>

  <div class="person">
    <p class="person__name">Dana Whitlock</p>
    <p class="person__title">Owner &amp; Manager</p>
  </div>

  <div class="divider"></div>

  <ul class="contact">
    <li>
      <svg viewBox="0 0 24 24" aria-hidden="true"><path d="M6.6 10.8a15 15 0 0 0 6.6 6.6l2.2-2.2a1 1 0 0 1 1-.25 11.4 11.4 0 0 0 3.6.57 1 1 0 0 1 1 1V20a1 1 0 0 1-1 1A17 17 0 0 1 3 4a1 1 0 0 1 1-1h3.5a1 1 0 0 1 1 1c0 1.25.2 2.45.57 3.57a1 1 0 0 1-.25 1z"/></svg>
      15550142087
    </li>
    <li>
      <svg viewBox="0 0 24 24" aria-hidden="true"><path d="M2 5h20v14H2z M2 5l10 8 10-8" /></svg>
      info@harborviewabb.com
    </li>
    <li>
      <svg viewBox="0 0 24 24" aria-hidden="true"><circle cx="12" cy="12" r="10"/></svg>
      www.harborviewabb.com
    </li>
  </ul>

  <p class="address">P.O. Box Linden Street Country Name AB, T2K 7M1</p>
</section>

<section class="card card--back" aria-label="Business card back">
  <div class="brand">
    <span class="brand__dot"></span>
    <span class="brand__name">Harborview Animal<br>Blood Bank</span>
  </div>
</section>

</body>
</html>
```